label design for cannabis

label template 4"x5.5" for a Massachusetts cannabis beverage product. labels will be transparent and placed on a blue (pantone 306C) bag.
https://www.fravostones.com/

Target Market(s)

cannabis customers in MA, 21+

Industry/Entity Type

cannabis consumer product

Font styles to use
Other font styles liked:
• DIN

Colors
0094D4
00A9DD
6FCCEA
C7EBF8
E9F6FB

Requirements
Must have
• label design with fravo logo, flavor (lemon, lime, plain, and coffee). 306C pantone for background and 11-0601 TCX for text. font=DINackground.
Nice to have
• tray icon, illustrated ice cubes in white (clear), yellow (lemon), green (lime) and brown (coffee)
Should not have
• no cartoonish characters

```html
<!DOCTYPE html>
<html lang="en">
<head>
<meta charset="utf-8">
<title>fravo infused ice cubes – lemon label</title>
<link rel="stylesheet" href="https://fonts.googleapis.com/css2?family=Barlow:wght@400;500;600;700&family=Barlow+Condensed:wght@500;600;700;800&display=swap">
<style>
  :root {
    --sky: #c7ebf8;
    --navy: #1f3366;
    --white: #ffffff;
    --lemon: #f4e81c;
    --ink: #1d1d1b;
    --panel-light: #eaf5fb;
    --alert-red: #e32526;
    --caution: #ddb02f;
  }
  * { margin: 0; padding: 0; box-sizing: border-box; }
  html, body { width: 1200px; height: 1200px; overflow: hidden; }
  body {
    position: relative;
    background: var(--sky);
    font-family: "Barlow", sans-serif;
    color: var(--white);
  }
  .label { position: absolute; background: var(--navy); }
  .label--front { left: 31px; top: 74px; width: 560px; height: 770px; }
  .label--back { left: 608px; top: 355px; width: 561px; height: 770px; }

  .front-frame {
    position: absolute; left: 24px; top: 22px; width: 511px; height: 726px;
    border: 3px solid var(--white); border-radius: 30px;
  }
  .brand {
    position: absolute; left: 0; width: 100%; top: 90px; text-align: center;
    font-family: "Barlow Condensed", sans-serif; font-weight: 800;
    font-size: 130px; line-height: 1; color: var(--white); letter-spacing: -1px;
  }
  .tagline {
    position: absolute; left: 0; width: 100%; top: 214px; text-align: center;
    font-family: "Barlow Condensed", sans-serif; font-weight: 600;
    font-size: 38px; line-height: 1; color: var(--white);
  }
  .cubes-art {
    position: absolute; left: 181px; top: 277px; width: 201px; height: 194px;
    background: radial-gradient(circle at 50% 50%, rgba(244,232,28,0.35), rgba(244,232,28,0.12));
    border-radius: 16px;
  }
  .flavor-rule {
    position: absolute; left: 216px; top: 501px; width: 127px; height: 2px; background: var(--lemon);
  }
  .flavor {
    position: absolute; left: 0; width: 100%; top: 505px; text-align: center;
    font-weight: 700; font-size: 33px; color: var(--lemon); letter-spacing: 1px;
  }
  .tray { position: absolute; left: 56px; top: 627px; width: 210px; height: 58px; }
  .tray-text {
    position: absolute; left: 56px; top: 629px; width: 208px; text-align: center;
    font-size: 15px; font-weight: 500; letter-spacing: 0.3px;
  }
  .age-badge {
    position: absolute; left: 420px; top: 609px; width: 92px; height: 92px;
    border: 4px solid var(--white); border-radius: 50%; text-align: center;
  }
  .age-badge__label {
    display: block; margin-top: 16px; font-family: "Barlow Condensed", sans-serif;
    font-weight: 600; font-size: 16px; line-height: 1;
  }
  .age-badge__value {
    display: block; font-weight: 700; font-size: 36px; line-height: 1;
  }
  .website {
    position: absolute; left: 0; width: 100%; top: 722px; text-align: center;
    font-size: 11px; letter-spacing: 0.3px;
  }

  .warning-strip {
    position: absolute; left: 27px; top: 590px; width: 508px; height: 120px;
    background: var(--panel-light); border: 4px solid var(--ink); border-radius: 24px;
    color: var(--ink);
  }
  .warning-icons { position: absolute; left: 0; top: 0; width: 500px; height: 112px; }
  .thc-caption {
    position: absolute; left: 14px; top: 87px; width: 92px; text-align: center;
    font-size: 11px; letter-spacing: 0.3px; line-height: 1;
  }
  .kids-text {
    position: absolute; left: 124px; top: 39px; width: 84px; text-align: center;
    font-weight: 700; font-size: 11px; line-height: 14px; letter-spacing: 0.2px;
  }
  .bag-notice {
    position: absolute; left: 334px; top: 15px; width: 162px;
    font-size: 9.6px; line-height: 11.8px; white-space: nowrap;
  }
  .bag-notice strong { display: block; margin-top: 10px; font-weight: 700; }
</style>
</head>
<body>
  <section class="label label--front">
    <div class="front-frame"></div>
    <div class="brand">fravo</div>
    <div class="tagline">infused ice cubes</div>
    <div class="cubes-art" role="img" aria-label="Yellow line illustration of three ice cubes"></div>
    <div class="flavor-rule"></div>
    <div class="flavor">lemon</div>
    <svg class="tray" viewBox="0 0 210 58" aria-hidden="true">
      <g fill="none" stroke="#ffffff" stroke-width="2.5">
        <rect x="1.5" y="1.5" width="205" height="24"/>
        <path d="M8 26 L11 55 L41 55 L44 26"/>
        <path d="M48 26 L51 55 L81 55 L84 26"/>
        <path d="M88 26 L91 55 L121 55 L124 26"/>
        <path d="M128 26 L131 55 L161 55 L164 26"/>
        <path d="M168 26 L171 55 L199 55 L202 26"/>
      </g>
    </svg>
    <div class="tray-text">50 mg per cube</div>
    <div class="age-badge">
      <span class="age-badge__label">FOR AGE</span>
      <span class="age-badge__value">21+</span>
    </div>
    <div class="website">www.fravostones.com</div>
  </section>

  <section class="label label--back">
    <div class="warning-strip">
      <svg class="warning-icons" viewBox="0 0 500 112" aria-hidden="true">
        <path d="M60 13 L98 79 L22 79 Z" fill="none" stroke="#e32526" stroke-width="3" stroke-linejoin="round"/>
        <circle cx="60" cy="58" r="10" fill="#1d1d1b"/>
        <path d="M138 17 L194 17 L208 43 L208 67 L194 93 L138 93 L124 67 L124 43 Z" fill="none" stroke="#e32526" stroke-width="6" stroke-linejoin="round"/>
        <rect x="152" y="24" width="28" height="6" rx="3" fill="#1d1d1b"/>
        <rect x="152" y="81" width="28" height="6" rx="3" fill="#1d1d1b"/>
        <rect x="228" y="15" width="3.5" height="80" fill="#1d1d1b"/>
        <path d="M286 26 L319 85 L253 85 Z" fill="#ddb02f" stroke="#1d1d1b" stroke-width="2" stroke-linejoin="round"/>
        <path d="M283 46 L289 46 L287.5 68 L284.5 68 Z" fill="#ffffff" stroke="#1d1d1b" stroke-width="1.5"/>
        <circle cx="286" cy="74" r="3" fill="#ffffff" stroke="#1d1d1b" stroke-width="1.5"/>
      </svg>
      <div class="thc-caption">CONTAINS THC</div>
      <div class="kids-text">NOT SAFE<br>FOR KIDS</div>
      <p class="bag-notice">To avoid danger of suffocation<br>keep this plastic bag away<br>from babies and children.<br>Do not use this bag in cribs,<br>beds, carriages, or play pens.<strong>THIS BAG IS NOT A TOY</strong></p>
    </div>
  </section>
</body>
</html>
```